New Alcoholic Spiked Seltzer Line

We need a can design for a line of low calorie alcoholic seltzer. This product is a sparkling water and vodka drink with no sugar added in a slim 12 oz can.

This is a lighter, healthier, alternative to the sugary ready-to-drinks on the market. The product contains only 3 ingredients: Vodka, Water and Natural Flavors. It has only 100 calories but still has 5% alcohol, so you don't need to sacrifice alcohol to cut calories.

This product also does not contain any preservatives.

We want this design to communicate the following objectives to the consumer and in this order:

1. Appetizing product
2.Low calorie
3.Communicate the type of beverage (Spiked Seltzer)

The brand name of the product is VELKA.

The flavor of the product needed to be used for the design is Mango-Orange.

Comparable products are:

www.brisavelfizz.example/
https://www.tarnowbubble.example
https://quellrind.example/

The designs should not infringe or copy the creative directions of the products mentionned above. They are only given so that you can better understand the type of product we are developing.

Target Market(s)

Young Professional women between the ages of 25 and 44

Industry/Entity Type

Product

Colors

Designer to choose colors to be used in the design.

Requirements
Must have
• Design extendibility, meaning it can be adapted for other flavors.
• This is a new category in the market we are targeting, so consumers must easily be able to identify what type of product this is.

```html
<!DOCTYPE html>
<html lang="en">
<head>
<meta charset="utf-8">
<title>VELKA Spiked Seltzer – Mango-Orange Can Label</title>
<link rel="stylesheet" href="https://fonts.googleapis.com/css2?family=Roboto+Mono:wght@500;700&family=Roboto+Condensed:wght@400;500&family=Raleway:wght@600&family=Pinyon+Script&family=Arimo:wght@400;700&family=Archivo+Black&display=swap">
<style>
  :root {
    --ink: #111111;
    --paper: #ffffff;
    --stage: #efefef;
    --mango: #ff8c2e;
    --coral: #f45f6e;
    --melon: #f26d6d;
    --rule: #222222;
    --box-line: #f7a27a;
    --sunset: linear-gradient(90deg, var(--mango), var(--coral) 50%, var(--mango));
  }
  * { box-sizing: border-box; margin: 0; padding: 0; }
  html, body { width: 1200px; height: 1200px; overflow: hidden; background: var(--stage); }
  .canvas { position: relative; width: 1200px; height: 1200px; }

  .label { position: absolute; background: var(--paper); overflow: hidden; color: var(--ink); }
  .label--front { left: 162px; top: 158px; width: 380px; height: 842px; }
  .label--back  { left: 613px; top: 192px; width: 379px; height: 816px; }

  .label__band { position: absolute; left: 0; top: 0; width: 100%; height: 12px; background: var(--sunset); }
  .label__pennants { position: absolute; left: 0; top: 28px; width: 100%; height: 16px; }
  .label__shapes { position: absolute; inset: 0; width: 100%; height: 100%; }

  /* front */
  .art { position: absolute; }
  .art--fountain { left: 47px; top: 81px; width: 285px; height: 82px;
    background: radial-gradient(ellipse at 50% 80%, var(--coral), var(--mango) 60%, rgba(255,140,46,0) 72%); }
  .art--sirens { left: 68px; top: 322px; width: 237px; height: 260px;
    background: linear-gradient(180deg, #222 0%, var(--coral) 35%, var(--mango) 55%, #111 80%);
    border-radius: 40% 40% 30% 30%; }
  .brand-word { position: absolute; left: 0; width: 100%; text-align: center;
    font-family: "Roboto Mono", monospace; font-weight: 700; color: var(--ink); }
  .brand-word--front { top: 160px; font-size: 48px; letter-spacing: 4px; line-height: 1; }
  .category-tags { position: absolute; top: 254px; left: 0; width: 100%; display: flex; justify-content: center; gap: 18px; }
  .category-tags span { background: var(--ink); color: var(--paper); font-family: "Roboto Mono", monospace;
    font-weight: 700; font-size: 18px; letter-spacing: 1.5px; padding: 1px 4px; line-height: 22px; }
  .tagline { position: absolute; top: 612px; left: 0; width: 100%; text-align: center;
    font-family: "Pinyon Script", cursive; font-size: 28px; color: var(--ink); }
  .flavor { position: absolute; top: 652px; left: 0; width: 100%; text-align: center;
    font-family: "Raleway", sans-serif; font-weight: 600; font-size: 23px; letter-spacing: 3px; color: var(--melon); }
  .calories { position: absolute; top: 712px; left: 0; width: 100%; text-align: center;
    font-family: "Roboto Condensed", sans-serif; font-weight: 500; font-size: 26px; }
  .abv { position: absolute; top: 746px; left: 0; width: 100%; text-align: center;
    font-family: "Arimo", sans-serif; font-size: 17px; letter-spacing: 1px; }

  /* back */
  .brand-word--back { top: 76px; font-size: 34px; letter-spacing: 5px; line-height: 1; }
  .subtitle { position: absolute; top: 114px; left: 0; width: 100%; text-align: center;
    font-family: "Roboto Mono", monospace; font-weight: 700; font-size: 23px; letter-spacing: 2px; }
  .story { position: absolute; left: 0; width: 100%; text-align: center;
    font-family: "Roboto Mono", monospace; font-weight: 500; font-size: 12.5px; letter-spacing: 1px; line-height: 16px; }
  .story--one { top: 150px; }
  .story--two { top: 229px; }
  .ingredients__title { position: absolute; top: 300px; left: 0; width: 100%; text-align: center;
    font-family: "Roboto Mono", monospace; font-weight: 700; font-size: 12px; letter-spacing: 1.5px; }
  .ingredient { position: absolute; top: 326px; width: 90px; text-align: center; }
  .ingredient--water { left: 48px; }
  .ingredient--flavors { left: 147px; }
  .ingredient--vodka { left: 242px; }
  .ingredient__icon { display: block; width: 60px; height: 60px; margin: 0 auto; border: 1px solid var(--box-line); background: var(--paper); }
  .ingredient__icon--art { background: radial-gradient(circle at 55% 45%, #ddd 0 22%, #222 24% 38%, var(--paper) 42%); }
  .ingredient__name { display: block; margin-top: 10px; font-family: "Roboto Mono", monospace; font-size: 14px; letter-spacing: 1px; line-height: 13px; }
  .ingredient--flavors .ingredient__name { margin-top: 4px; }

  .nutrition { position: absolute; left: 107px; top: 466px; width: 179px; height: 324px;
    border: 1px solid #555; padding: 4px 9px; font-family: "Arimo", sans-serif; font-size: 8.5px; line-height: 1.2; background: var(--paper); }
  .nutrition__title { font-family: "Archivo Black", sans-serif; font-size: 19px; line-height: 1; letter-spacing: -0.2px; }
  .nutrition__row { display: flex; justify-content: space-between; border-top: 1px solid var(--rule); padding: 2px 0 3px; }
  .nutrition__row--indent { padding-left: 10px; }
  .nutrition__row--thick { border-top-width: 5px; }
  .nutrition__row--mid { border-top-width: 3px; }
  .nutrition__row--plain { border-top: none; }
  .nutrition b { font-weight: 700; }
  .nutrition__note { border-top: 1px solid var(--rule); padding-top: 3px; font-size: 8.3px; line-height: 1.35; }
</style>
</head>
<body>
<main class="canvas">

  <!-- Front label -->
  <section class="label label--front">
    <div class="label__band"></div>
    <svg class="label__pennants" viewBox="0 0 380 16" aria-hidden="true">
      <g fill="#111">
        <polygon points="7,2 17,2 12,13"/><polygon points="34,2 44,2 39,13"/><polygon points="61,2 71,2 66,14"/>
        <polygon points="88,3 98,3 93,15"/><polygon points="115,3 125,3 120,15"/><polygon points="142,4 152,4 147,16"/>
        <polygon points="169,4 179,4 174,16"/><polygon points="196,4 206,4 201,16"/><polygon points="223,4 233,4 228,16"/>
        <polygon points="250,3 260,3 255,15"/><polygon points="277,3 287,3 282,15"/><polygon points="304,2 314,2 309,14"/>
        <polygon points="331,2 341,2 336,13"/><polygon points="358,1 368,1 363,12"/>
      </g>
    </svg>

    <div class="art art--fountain" role="img" aria-label="Orange and coral fountain flourish crowning the brand name"></div>
    <h1 class="brand-word brand-word--front">VELKA</h1>
    <div class="category-tags"><span>Spiked</span><span>Seltzer</span></div>
    <div class="art art--sirens" role="img" aria-label="Illustration of two mirrored mermaids with mango-orange hair"></div>

    <p class="tagline">Naturally Flavored</p>
    <p class="flavor">MANGO-ORANGE</p>
    <p class="calories">Only 100 CAL.</p>
    <p class="abv">5% alc./vol.</p>

    <svg class="label__shapes" viewBox="0 0 380 842" aria-hidden="true">
      <defs>
        <linearGradient id="sunsetFront" x1="0" x2="1" y1="0" y2="0">
          <stop offset="0" stop-color="#ff8c2e"/><stop offset="0.5" stop-color="#f45f6e"/><stop offset="1" stop-color="#ff8c2e"/>
        </linearGradient>
      </defs>
      <polygon points="8,700 54,730 8,738" fill="#ff8c2e"/>
      <polygon points="8,766 72,766 8,808" fill="#111"/>
      <polygon points="330,686 374,683 374,722" fill="#ff8c2e"/>
      <polygon points="308,758 374,762 374,810" fill="#111"/>
      <polygon points="47,842 226,798 380,842" fill="url(#sunsetFront)"/>
    </svg>
  </section>

  <!-- Back label -->
  <section class="label label--back">
    <div class="label__band"></div>
    <svg class="label__pennants" viewBox="0 0 379 16" aria-hidden="true">
      <g fill="#111">
        <polygon points="10,2 20,2 15,13"/><polygon points="37,2 47,2 42,14"/><polygon points="64,3 74,3 69,15"/>
        <polygon points="91,3 101,3 96,15"/><polygon points="118,4 128,4 123,16"/><polygon points="145,4 155,4 150,16"/>
        <polygon points="172,4 182,4 177,16"/><polygon points="199,4 209,4 204,16"/><polygon points="226,4 236,4 231,16"/>
        <polygon points="253,3 263,3 258,15"/><polygon points="280,3 290,3 285,15"/><polygon points="307,2 317,2 312,14"/>
        <polygon points="334,1 344,1 339,13"/><polygon points="361,0 371,0 366,12"/>
      </g>
    </svg>

    <h2 class="brand-word brand-word--back">VELKA</h2>
    <p class="subtitle">Spiked Seltzer</p>
    <p class="story story--one">text texdt texttext text text<br>text text texttgfext text text<br>text text texttefghft text texttext<br>dgshogoeigyioshoi eagi</p>
    <p class="story story--two">text text texttefghft text texttext<br>dgshogoeigyioshoi eagi</p>

    <p class="ingredients__title">MADE WITH 3 INGREDIENTS</p>
    <div class="ingredient ingredient--water">
      <svg class="ingredient__icon" viewBox="0 0 60 60" aria-hidden="true">
        <path d="M30 14 C26 24 20 30 20 38 A10 10 0 0 0 40 38 C40 30 34 24 30 14 Z" fill="none" stroke="#111" stroke-width="3"/>
        <path d="M26 38 A4 5 0 0 0 30 44" fill="none" stroke="#111" stroke-width="2"/>
      </svg>
      <span class="ingredient__name">Water</span>
    </div>
    <div class="ingredient ingredient--flavors">
      <span class="ingredient__icon ingredient__icon--art" role="img" aria-label="Fruit splash illustration"></span>
      <span class="ingredient__name">Natural<br>Flavors</span>
    </div>
    <div class="ingredient ingredient--vodka">
      <svg class="ingredient__icon" viewBox="0 0 60 60" aria-hidden="true">
        <polygon points="14,12 46,12 30,32" fill="#111"/>
        <rect x="29" y="31" width="2" height="17" fill="#111"/>
        <rect x="21" y="47" width="18" height="2.5" fill="#111"/>
      </svg>
      <span class="ingredient__name">Vodka</span>
    </div>

    <div class="nutrition">
      <div class="nutrition__title">Nutrition Facts</div>
      <div class="nutrition__row nutrition__row--plain">Serving Size 100 g</div>
      <div class="nutrition__row nutrition__row--thick">Amount Per Serving</div>
      <div class="nutrition__row"><span>Calories 250</span><span>Calories from fat 10</span></div>
      <div class="nutrition__row nutrition__row--mid" style="justify-content:flex-end"><b>% Daily Value*</b></div>
      <div class="nutrition__row"><span><b>Total Fat</b> 4%</span><span>4%</span></div>
      <div class="nutrition__row nutrition__row--indent"><span>Saturated Fat 1.5%</span><span>4%</span></div>
      <div class="nutrition__row nutrition__row--indent"><span>Trans Fat</span><span></span></div>
      <div class="nutrition__row"><span><b>Cholesterol</b> 50mg</span><span>28%</span></div>
      <div class="nutrition__row"><span><b>Sodium</b> 150mg</span><span>15%</span></div>
      <div class="nutrition__row"><span><b>Total Carbohydrate</b> 10g</span><span>3%</span></div>
      <div class="nutrition__row nutrition__row--indent"><span>Dietary Fiber 5g</span><span></span></div>
      <div class="nutrition__row nutrition__row--indent"><span>Sugars 3g</span><span></span></div>
      <div class="nutrition__row"><span><b>Protein</b> 16%</span><span></span></div>
      <div class="nutrition__row nutrition__row--thick"><span><b>Vitamin A</b> &nbsp;1% &nbsp;•&nbsp; <b>Vitamin C</b> &nbsp;3%</span></div>
      <div class="nutrition__row"><span><b>Calcium</b> &nbsp;2% &nbsp;&nbsp;•&nbsp; <b>Iron</b> 2%</span></div>
      <p class="nutrition__note">*Percent Daily Values are based on a 2,000 calorie diet. Your daily values may be higher or lower depending on your calorie needs.</p>
    </div>

    <svg class="label__shapes" viewBox="0 0 379 816" aria-hidden="true" style="pointer-events:none">
      <defs>
        <linearGradient id="sunsetBack" x1="0" x2="1" y1="1" y2="0">
          <stop offset="0" stop-color="#ff8c2e"/><stop offset="1" stop-color="#f45f6e"/>
        </linearGradient>
      </defs>
      <polygon points="323,474 379,400 379,472" fill="url(#sunsetBack)"/>
      <polygon points="318,516 376,504 376,536" fill="#111"/>
      <polygon points="2,644 58,660 2,688" fill="url(#sunsetBack)"/>
      <polygon points="2,712 71,692 2,788" fill="#111"/>
    </svg>
  </section>

</main>
</body>
</html>
```